Small boutique multi-family apartment developer needs premium website design.

We are a growing real estate development company specializing in multi family apartment development. Our company Mireval Stone Development focuses on passive real estate investors looking to maximize their current real estate portfolio by allowing us to develop and reposition their current properties allowing them more cashflow while we are also able to take over the management of their asset in order to ensure optimal performance on a consistent basis.

```html
<!DOCTYPE html>
<html lang="en">
<head>
<meta charset="utf-8">
<title>Mireval Stone Development</title>
<link href="https://fonts.googleapis.com/css2?family=Michroma&family=Lato:wght@400;700&display=swap" rel="stylesheet">
<style>
:root{
  --navy:#1f2433;
  --navy-deep:#181c28;
  --mauve:#c8aeb1;
  --mauve-light:#d9c3c5;
  --ink:#1c1f28;
  --text:#555a63;
  --line:#d8d8dc;
  --white:#ffffff;
}
*{box-sizing:border-box;margin:0;padding:0}
html,body{width:1200px;height:4754px;overflow:hidden}
body{font-family:"Lato",sans-serif;color:var(--text);background:var(--white);position:relative}
.display{font-family:"Michroma",sans-serif;text-transform:uppercase;color:var(--ink)}
.accent{color:var(--mauve)}
.btn{display:inline-block;background:var(--mauve);color:var(--white);font-family:"Michroma",sans-serif;font-size:14px;text-transform:uppercase;padding:16px 32px;letter-spacing:.5px;text-decoration:none}
section,header,footer{position:absolute;left:0;width:1200px}

/* header */
.site-header{top:0;height:123px;background:var(--white);border-bottom:1px solid var(--line)}
.topbar{position:absolute;right:0;top:0;width:660px;height:52px;background:var(--navy);clip-path:polygon(30px 0,100% 0,100% 100%,0 100%);display:flex;align-items:center;gap:36px;padding-left:90px;color:var(--white);font-family:"Michroma",sans-serif;font-size:12px}
.brand{position:absolute;left:110px;top:24px;display:flex;align-items:center;gap:12px;font-family:"Lato",sans-serif;font-weight:700;font-size:30px;color:var(--navy)}
.brand .mark{width:22px;height:22px;background:var(--mauve)}
.nav{position:absolute;left:432px;top:78px;display:flex;gap:56px;font-family:"Michroma",sans-serif;font-size:12px;color:var(--ink);align-items:center}
.nav .active{text-decoration:underline}
.nav-cta{position:absolute;left:946px;top:70px;background:var(--mauve);color:var(--white);font-family:"Michroma",sans-serif;font-size:12px;padding:12px 20px}

/* hero */
.hero{top:123px;height:549px;background:linear-gradient(180deg,#4f5664 0%,#6b6357 45%,#55613f 100%);text-align:center}
.hero h1{position:absolute;top:170px;width:100%;font-family:"Michroma",sans-serif;color:var(--white);font-size:40px;line-height:64px;text-transform:uppercase;font-weight:400}
.hero .btn{position:absolute;left:489px;top:308px;border:2px solid var(--white);padding:16px 24px;font-size:15px}
.dots{position:absolute;top:483px;left:0;width:100%;display:flex;justify-content:center;gap:10px}
.dots span{width:11px;height:11px;border-radius:50%;background:rgba(255,255,255,.55)}
.dots span.on{background:var(--white)}

/* about */
.about{top:672px;height:480px;text-align:center}
.about h2{margin-top:70px;font-size:40px;font-weight:400}
.about p{width:860px;margin:30px auto 0;font-size:15.5px;line-height:31px}
.about p + p{margin-top:20px}
.about .btn{margin-top:40px}

.mission{top:1160px;height:240px;text-align:center}
.mission h2{font-size:39px;font-weight:400;line-height:62px}

/* feature rows */
.feature{height:532px}
.feature .photo{position:absolute;top:0;width:600px;height:532px}
.feature .copy{position:absolute;top:60px;width:440px}
.feature .num{font-family:"Michroma",sans-serif;font-size:30px;color:var(--mauve-light)}
.feature h3{font-family:"Lato",sans-serif;font-weight:700;font-size:25px;color:var(--ink);margin:14px 0 18px}
.feature p{font-size:14px;line-height:29px}
.feature p + p{margin-top:28px}
.feature .btn{margin-top:28px}
.f1{top:1403px}.f2{top:1935px}.f3{top:2467px}

/* stats */
.stats{top:3112px;height:338px;background:var(--navy)}
.stat{position:absolute;top:78px;width:200px;text-align:center;color:var(--white)}
.stat .ring{width:138px;height:138px;margin:0 auto;border-radius:50%;border:10px solid #4a4e5c;background:#d9c8ca;display:flex;align-items:center;justify-content:center;font-size:38px;color:var(--ink)}
.stat .label{margin-top:22px;font-size:23px}

/* listings */
.listings{top:3450px;height:870px}
.listings h2{text-align:center;margin-top:80px;font-size:38px;font-weight:400}
.listing-photo{position:absolute;left:140px;top:163px;width:920px;height:436px;border-radius:14px;background:linear-gradient(180deg,#1e3a6e 0%,#4d6fa6 40%,#c9c6c0 70%,#5a5750 100%)}
.listing-card{position:absolute;left:204px;top:488px;width:792px;height:304px;background:var(--white);border-radius:16px;box-shadow:0 2px 12px rgba(0,0,0,.12);text-align:center;padding-top:34px}
.listing-card .date{font-size:14px;color:var(--mauve)}
.listing-card h3{font-family:"Michroma",sans-serif;font-weight:400;font-size:22px;color:var(--ink);margin:14px 0 12px}
.listing-card p{width:680px;margin:0 auto;font-size:14px;line-height:31px;color:var(--ink)}
.listing-card a{display:inline-block;margin-top:18px;font-family:"Michroma",sans-serif;font-size:14px;color:var(--ink);text-decoration:underline}

/* footer */
.site-footer{top:4320px;height:434px;background:var(--navy);color:var(--white)}
.site-footer h4{font-family:"Michroma",sans-serif;font-weight:400;font-size:14px;position:absolute;top:80px}
.links{position:absolute;left:110px;top:126px;list-style:none;font-size:13px}
.links li{height:33px}
.links li::before{content:"»";margin-right:14px}
.contact{position:absolute;left:320px;top:122px;font-size:12.5px}
.contact .row{display:flex;align-items:center;gap:16px;height:66px;margin-top:-14px}
.contact .row:first-child{margin-top:0}
.contact .icon{width:38px;height:38px;border:1.5px solid var(--white);border-radius:50%;display:flex;align-items:center;justify-content:center;flex:none}
.form{position:absolute;left:638px;top:118px;width:450px}
.form .field{background:var(--white);color:#888;font-size:11px;padding:0 12px;height:32px;line-height:32px}
.form .pair{display:flex;gap:8px}
.form .pair .field{flex:1}
.form .field + .field,.form .pair + .field{margin-top:10px}
.form .message{height:72px;line-height:20px;padding-top:6px}
.form .submit{position:absolute;right:0;top:200px;width:124px;height:34px;background:var(--mauve);border:1px solid var(--white);font-family:"Michroma",sans-serif;font-size:10px;display:flex;align-items:center;justify-content:center}
.footer-rule{position:absolute;left:110px;top:352px;width:980px;height:1px;background:#3a3f4e}
.copyright{position:absolute;left:110px;top:386px;font-size:12px}
.social{position:absolute;left:978px;top:376px;display:flex;gap:10px}
.social span{width:32px;height:32px;border-radius:50%;border:1.5px solid var(--white)}
</style>
</head>
<body>

<header class="site-header">
  <div class="topbar">
    <span>Call : (555) 014-2270</span>
    <span>Email : hello@mirevalstone.com</span>
  </div>
  <div class="brand"><span>Mireval Stone Development</span><span class="mark"></span></div>
  <nav class="nav">
    <span class="active">Home</span><span>About</span><span>News</span><span>Contact Us</span>
    <svg width="16" height="16" viewBox="0 0 16 16"><circle cx="6.5" cy="6.5" r="5" fill="none" stroke="#1c1f28" stroke-width="1.8"/><line x1="10.2" y1="10.2" x2="15" y2="15" stroke="#1c1f28" stroke-width="1.8"/></svg>
  </nav>
  <span class="nav-cta">Contact Us</span>
</header>

<section class="hero" role="img" aria-label="Large suburban two-storey house with stone facade, garage doors and front lawn">
  <h1>Welcome to<br>Mireval Stone Development</h1>
  <span class="btn">Get Started</span>
  <div class="dots"><span></span><span class="on"></span><span></span><span></span></div>
</section>

<section class="about">
  <h2 class="display">About <span class="accent">MSD</span></h2>
  <p>Mireval Stone Development was created to satisfy the overwhelming request to help our clients who want to invest in long term buy and hold Real Estate, and create a more profitable and balanced investment portfolio. We offer opportunities to invest in cash flowing Multi-Family apartment building investments in the Southern California area.</p>
  <p>"Many of our clients are looking to diversify their retirement portfolio, but don't know the ins and outs of how to invest in Managed Real Estate investments."</p>
  <span class="btn">Read More</span>
</section>

<section class="mission">
  <h2 class="display">Committed to the<br><span class="accent">Fundamentals of Investing, to</span><br>Ensure Longterm Growth</h2>
</section>

<section class="feature f1">
  <div class="copy" style="left:112px">
    <div class="num">01</div>
    <h3>Apartment Building Optimization</h3>
    <p>We offer opportunities to invest in cash flowing Multi-Family<br>apartment building investments in the Southern<br>California area.</p>
    <p>Mireval Stone Development was created to satisfy the overwhelming request to help our clients who want to invest in long term buy and hold Real Estate, and create a more profitable and balanced investment portfolio.</p>
    <span class="btn">Read More</span>
  </div>
  <div class="photo" style="left:600px;background:linear-gradient(180deg,#3f6fb5 0%,#8fb3dc 45%,#8a8f9a 80%,#4d5a3c 100%)" role="img" aria-label="Modern multi-storey apartment building at dusk"></div>
</section>

<section class="feature f2">
  <div class="photo" style="left:0;background:linear-gradient(135deg,#2a2420 0%,#7a5a3c 40%,#e0902e 65%,#2b2a30 100%)" role="img" aria-label="Miniature house models beside glowing bar chart on a tablet"></div>
  <div class="copy" style="left:654px">
    <div class="num">02</div>
    <h3>Real Estate Portfolio Management</h3>
    <p>We offer opportunities to invest in cash flowing Multi-Family<br>apartment building investments in the Southern<br>California area.</p>
    <p>Mireval Stone Development was created to satisfy the overwhelming request to help our clients who want to invest in long term buy and hold Real Estate, and create a more profitable and balanced investment portfolio.</p>
    <span class="btn">Read More</span>
  </div>
</section>

<section class="feature f3">
  <div class="copy" style="left:114px">
    <div class="num">03</div>
    <h3>Private Lending</h3>
    <p>We offer opportunities to invest in cash flowing Multi-Family<br>apartment building investments in the Southern<br>California area.</p>
    <p>Mireval Stone Development was created to satisfy the overwhelming request to help our clients who want to invest in long term buy and hold Real Estate, and create a more profitable and balanced investment portfolio.</p>
    <span class="btn">Read More</span>
  </div>
  <div class="photo" style="left:602px;background:linear-gradient(135deg,#b89a78 0%,#d8cfc4 45%,#9aa3b3 75%,#3a3f4a 100%)" role="img" aria-label="Desk with financial reports, calculator and laptop during a meeting"></div>
</section>

<section class="stats">
  <div class="stat" style="left:118px"><div class="ring">02</div><div class="label">Partners</div></div>
  <div class="stat" style="left:371px"><div class="ring">06</div><div class="label">Employees</div></div>
  <div class="stat" style="left:627px"><div class="ring">33%</div><div class="label">Investments</div></div>
  <div class="stat" style="left:880px"><div class="ring">100</div><div class="label">Success</div></div>
</section>

<section class="listings">
  <h2 class="display">Properties <span class="accent">Listings</span></h2>
  <div class="listing-photo" role="img" aria-label="Modern white hillside home with lit terrace at twilight"></div>
  <article class="listing-card">
    <div class="date">20 FEB 2022</div>
    <h3>Bold and Breathtaking</h3>
    <p>Overlooking the Calder Bay bay and perched high above the private yacht clubs below, this Westcliff Estate has quickly become the conversation focal point of many of the Calder Bay locals "in the know".With sharp clean lines, and attention paid to every detail, you will quickly see why 3321 Alder Ave. is considered among many, to be the best new property to hit the market in Westcliff.</p>
    <a>Read More</a>
  </article>
</section>

<footer class="site-footer">
  <h4 style="left:110px">Useful Links</h4>
  <ul class="links"><li>Home</li><li>About</li><li>News</li><li>Services</li><li>Contact</li></ul>

  <h4 style="left:320px">Contact Information</h4>
  <div class="contact">
    <div class="row"><span class="icon"><svg width="14" height="18" viewBox="0 0 14 18"><path d="M7 1a6 6 0 0 1 6 6c0 4-6 10-6 10S1 11 1 7a6 6 0 0 1 6-6z" fill="none" stroke="#fff" stroke-width="1.5"/><circle cx="7" cy="7" r="2" fill="#fff"/></svg></span><span>1840 Harbor Crest Ave<br>Suite 310,Calder Bay, CA. 90417</span></div>
    <div class="row"><span class="icon"><svg width="16" height="16" viewBox="0 0 16 16"><path d="M3 1l3 3-2 2c1 2 3 4 5 5l2-2 3 3-2 3C7 15 1 9 1 3z" fill="none" stroke="#fff" stroke-width="1.4"/></svg></span><span>Phone : (555) 014-2270</span></div>
    <div class="row"><span class="icon"><svg width="16" height="12" viewBox="0 0 16 12"><rect x="1" y="1" width="14" height="10" fill="none" stroke="#fff" stroke-width="1.4"/><path d="M1 1l7 6 7-6" fill="none" stroke="#fff" stroke-width="1.4"/></svg></span><span>Email : hello@mirevalstone.com</span></div>
  </div>

  <h4 style="left:636px">Get in Touch</h4>
  <div class="form">
    <div class="pair"><div class="field">Name :</div><div class="field">Phone :</div></div>
    <div class="field">Email :</div>
    <div class="field message">Message :</div>
    <div class="submit">Submit</div>
  </div>

  <div class="footer-rule"></div>
  <div class="copyright">Copyrights © 2024 Mireval Stone Development. &nbsp;|&nbsp; Privacy policy</div>
  <div class="social"><span></span><span></span><span></span></div>
</footer>

</body>
</html>
```